Looking for a modern, Professional business card design

We have a simple business card, but are looking for a more modern, professional look. A sample of the basic card is attached as well as the logo. We would also like to add that we offer:
Struggling with your finances?
- Learn to become debt free
- Discover the power of cash
- Control your money instead of it controlling you
Let us help you achieve a new level of financial freedom!
Also, we would like to have a "SPECIAL OFFER!: FREE 30 minute consultation"
Financial Planning

```html
<!DOCTYPE html>
<html lang="en">
<head>
<meta charset="utf-8">
<title>Steady Harbor Coaching – Business Card</title>
<link href="https://fonts.googleapis.com/css2?family=Josefin+Sans:wght@400;600;700&family=Oswald:wght@600&display=swap" rel="stylesheet">
<style>
  :root {
    --green: #2b9a47;
    --green-dark: #1f7f38;
    --ink: #1c1c1c;
    --paper: #ffffff;
    --strip: #e6e8e7;
    --backdrop: #eceeed;
  }
  * { box-sizing: border-box; margin: 0; padding: 0; }
  html, body { width: 1200px; height: 900px; overflow: hidden; }
  body {
    background: var(--backdrop);
    font-family: "Josefin Sans", sans-serif;
    color: var(--ink);
    position: relative;
  }
  .card {
    position: absolute;
    left: 285px;
    width: 630px;
    height: 360px;
    background: var(--paper);
    box-shadow: 0 6px 20px rgba(0,0,0,0.12);
    overflow: hidden;
  }
  .card--back { top: 60px; }
  .card--front { top: 480px; }

  /* Back */
  .card__edge {
    position: absolute; right: 0; top: 0; bottom: 0;
    width: 22px; background: var(--green);
  }
  .offer-copy {
    position: absolute; left: 40px; top: 120px;
    font-size: 17px; line-height: 1.35;
  }
  .offer-copy__title { font-weight: 600; font-size: 19px; }
  .offer-copy__list { list-style: none; }
  .offer-copy__list li::before { content: "- "; }
  .offer-copy__cta { font-weight: 700; }
  .special-offer {
    margin-top: 8px;
    display: inline-block;
    background: var(--green);
    color: var(--paper);
    font-size: 15px;
    letter-spacing: 1px;
    padding: 4px 30px 2px 30px;
    width: 230px;
    text-align: center;
  }
  .special-offer__detail { font-size: 17px; font-weight: 600; }

  .brand {
    position: absolute;
    display: flex; align-items: center; gap: 10px;
  }
  .brand__dot { width: 22px; height: 22px; border-radius: 50%; background: var(--green); flex: none; }
  .brand__name { font-weight: 700; color: var(--ink); line-height: 1; }
  .brand__tagline { font-size: 11px; color: var(--green-dark); margin-top: 4px; }
  .card--back .brand { right: 50px; top: 48px; }
  .card--back .brand__name { font-size: 22px; }

  /* Front */
  .name-band {
    position: absolute; left: 0; top: 0; bottom: 0;
    width: 175px; background: var(--green);
    color: var(--paper);
  }
  .name-band__strip {
    position: absolute; left: 175px; top: 0; bottom: 0;
    width: 22px; background: var(--strip);
  }
  .name-band__text {
    position: absolute; left: 50%; top: 50%;
    transform: translate(-50%, -50%) rotate(-90deg);
    white-space: nowrap; text-align: center;
  }
  .name-band__name {
    font-family: "Oswald", sans-serif; font-weight: 600;
    font-size: 36px; letter-spacing: 1px; line-height: 1.05;
  }
  .name-band__role { font-size: 22px; letter-spacing: 0.5px; }

  .card--front .brand { left: 250px; top: 60px; }
  .card--front .brand__name { font-size: 30px; }
  .card--front .brand__dot { width: 30px; height: 30px; }

  .contacts { position: absolute; left: 250px; top: 205px; list-style: none; }
  .contacts__item {
    display: flex; align-items: center; gap: 14px;
    font-size: 17px; margin-bottom: 14px;
  }
  .contacts__icon {
    width: 26px; height: 26px; border-radius: 50%;
    background: var(--green); display: flex; align-items: center; justify-content: center;
    flex: none;
  }
</style>
</head>
<body>

<section class="card card--back">
  <div class="brand">
    <span class="brand__dot"></span>
    <div>
      <div class="brand__name">Steady Harbor Coaching</div>
      <div class="brand__tagline">Achieve a new level of personal freedom</div>
    </div>
  </div>
  <div class="offer-copy">
    <p class="offer-copy__title">Struggling with your finances?</p>
    <ul class="offer-copy__list">
      <li>Learn to become debt free</li>
      <li>Discover the power of cash</li>
      <li>Control your money instead of it controlling you</li>
    </ul>
    <p class="offer-copy__cta">Let us help you achieve a new level<br>of financial freedom!</p>
    <div class="special-offer">SPECIAL OFFER!</div>
    <p class="special-offer__detail">FREE 30 minute consultation</p>
  </div>
  <div class="card__edge"></div>
</section>

<section class="card card--front">
  <div class="name-band">
    <div class="name-band__text">
      <div class="name-band__name">DANIEL R. WHITCOMBE</div>
      <div class="name-band__role">Personal Financial Coach</div>
    </div>
  </div>
  <div class="name-band__strip"></div>

  <div class="brand">
    <span class="brand__dot"></span>
    <div>
      <div class="brand__name">Steady Harbor Coaching</div>
      <div class="brand__tagline">Achieve a new level of personal freedom</div>
    </div>
  </div>

  <ul class="contacts">
    <li class="contacts__item">
      <span class="contacts__icon">
        <svg width="14" height="14" viewBox="0 0 24 24" aria-hidden="true"><path fill="#fff" d="M6.6 10.8a15.1 15.1 0 0 0 6.6 6.6l2.2-2.2c.3-.3.7-.4 1-.2 1.1.4 2.3.6 3.6.6.6 0 1 .4 1 1V20c0 .6-.4 1-1 1A17 17 0 0 1 3 4c0-.6.4-1 1-1h3.5c.6 0 1 .4 1 1 0 1.3.2 2.5.6 3.6.1.3 0 .7-.2 1z"/></svg>
      </span>
      (205) 555-0147
    </li>
    <li class="contacts__item">
      <span class="contacts__icon">
        <svg width="14" height="14" viewBox="0 0 24 24" aria-hidden="true"><rect x="3" y="6" width="18" height="12" rx="1" fill="#fff"/><path d="M3 7l9 6 9-6" stroke="#2b9a47" stroke-width="1.6" fill="none"/></svg>
      </span>
      daniel@steadyharborcoach.com
    </li>
    <li class="contacts__item">
      <span class="contacts__icon">
        <svg width="14" height="14" viewBox="0 0 24 24" aria-hidden="true"><path fill="#fff" d="M12 2a7 7 0 0 0-7 7c0 5 7 13 7 13s7-8 7-13a7 7 0 0 0-7-7zm0 9.5A2.5 2.5 0 1 1 12 6.5a2.5 2.5 0 0 1 0 5z"/></svg>
      </span>
      www.steadyharborcoach.com
    </li>
  </ul>
</section>

</body>
</html>
```